Shampoo and Conditioner label design

We have a shampoo and conditioner line that we're looking to re-brand. We need the label re-designed to have a more appealing look. I have uploaded our logo and an example of our current design. We're looking for a design that advertises a more natural & and organic feel w/ natural, cool colors. A great bench mark which we're trying to emulate is Lumen Grove. They have great packaging for their products and they are attractive to a lot of people.

Target Market(s)

Natural hair. Ethnic hair.

Industry/Entity Type

Hair Care Product

Logo Text

Tidewell Curl Co.

Colors

Designer to choose colors to be used in the design.

Requirements
Must have
• Must describe what the product does for the individual making the purchase.
• - hydrating and moisturizing
• - improves healthy shine
• - strengthens hair
• - organic ingredients
• - Sulfate Free
• - Paraben Free
Nice to have
• an appealing design. welcoming with warm, natural colors. informative

```html
<!DOCTYPE html>
<html lang="en">
<head>
<meta charset="UTF-8">
<title>Tidewell Curl Co. — Lumen Grove Shampoo Label</title>
<link href="https://fonts.googleapis.com/css2?family=Tenor+Sans&display=swap" rel="stylesheet">
<style>
  :root {
    --label-bg: #eef1eb;
    --brand-green: #3f6b4c;
    --title-green: #7fa68a;
    --ornament-light: #c9dacd;
    --ornament-mid: #9fbfa8;
    --copy-grey: #6f7f73;
  }
  * { margin: 0; padding: 0; box-sizing: border-box; }
  html, body { width: 1200px; height: 1200px; overflow: hidden; }
  body {
    background: var(--label-bg);
    font-family: "Tenor Sans", sans-serif;
    position: relative;
  }
  .brand-name {
    position: absolute;
    left: 0; right: 0;
    top: 405px;
    text-align: center;
    color: var(--brand-green);
    font-size: 44px;
    line-height: 1.2;
  }
  .product-title {
    position: absolute;
    left: 0; right: 0;
    top: 584px;
    text-align: center;
    color: var(--title-green);
    font-size: 25px;
    font-weight: 400;
    line-height: 33px;
  }
  .benefit-ornament {
    position: absolute;
    left: 556px;
    top: 660px;
    width: 98px;
    height: 296px;
    border-radius: 8px;
    background: linear-gradient(180deg, var(--ornament-mid), var(--ornament-light));
  }
  .benefit {
    position: absolute;
    color: var(--copy-grey);
    font-size: 12.5px;
    line-height: 16px;
  }
  .benefit--left  { right: 652px; text-align: right; }
  .benefit--right { left: 662px; text-align: left; }
  .benefit--center { left: 0; right: 0; text-align: center; }
  .net-weight {
    position: absolute;
    left: 0; right: 0;
    top: 1030px;
    text-align: center;
    color: var(--copy-grey);
    font-size: 12px;
  }
</style>
</head>
<body>
  <div class="brand-name">Tidewell<br>Curl Co.</div>

  <h1 class="product-title">Lumen Grove<br>Shampoo</h1>

  <div class="benefit-ornament" role="img" aria-label="Green vine with alternating leaves running between the benefit list"></div>

  <p class="benefit benefit--left"  style="top:690px">Hydrating and<br>Moisturizing</p>
  <p class="benefit benefit--right" style="top:756px">Improves Healthy<br>Shine</p>
  <p class="benefit benefit--left"  style="top:794px">Organic<br>Ingredients</p>
  <p class="benefit benefit--right" style="top:840px">Strengthens<br>Hair</p>
  <p class="benefit benefit--left"  style="top:898px">Paraben<br>Free</p>
  <p class="benefit benefit--center" style="top:963px">Sulfate Free</p>

  <p class="net-weight">Net Wt.150 mL</p>
</body>
</html>
```